Self Serve Entertainment Stationary

Start up company requires matching stationary templates for Business Cards, letterhead and 'With Compliments' slips. The final design should keep with the style of our kiosk design, investor brochure and other collateral.

```html
<!DOCTYPE html>
<html lang="en">
<head>
<meta charset="utf-8">
<title>KioskPlay Entertainment Stationery</title>
<link rel="stylesheet" href="https://fonts.googleapis.com/css2?family=Roboto:ital,wght@0,400;0,700;1,700&family=Dancing+Script:wght@400&display=swap">
<style>
  :root {
    --brand-blue: #2476c2;
    --paper: #ffffff;
    --stage: #000000;
    --ink: #3a3a3a;
    --ink-soft: #555555;
    --map-pale: #e7ecf3;
    --map-on-blue: rgba(255,255,255,0.12);
  }
  * { box-sizing: border-box; margin: 0; padding: 0; }
  html, body { width: 1200px; height: 808px; overflow: hidden; }
  body { background: var(--stage); position: relative; font-family: "Roboto", sans-serif; color: var(--ink); }

  .brand { display: flex; align-items: center; gap: 12px; color: var(--paper); white-space: nowrap; }
  .brand-square { background: var(--paper); flex: none; }
  .brand-name { font-family: "Roboto", sans-serif; font-weight: 700; line-height: 1; }

  /* Letterhead */
  .letterhead { position: absolute; left: 32px; top: 34px; width: 523px; height: 740px; background: var(--paper); }
  .letterhead-header { height: 96px; background: var(--brand-blue); padding: 0 0 0 48px; display: flex; align-items: center; }
  .letterhead-header .brand-square { width: 26px; height: 26px; }
  .letterhead-header .brand-name { font-size: 26px; }
  .salutation { position: absolute; left: 48px; top: 130px; font-size: 10px; font-weight: 700; }
  .date-line { position: absolute; left: 396px; top: 130px; font-size: 10px; }
  .letter-body { position: absolute; left: 48px; top: 171px; width: 426px; font-size: 8.6px; line-height: 13px; text-align: justify; color: var(--ink-soft); }
  .letter-body p + p { margin-top: 12px; }
  .letter-body .indent { text-indent: 24px; }
  .sign-off { position: absolute; left: 396px; top: 647px; font-size: 8.5px; line-height: 13px; color: var(--ink-soft); }
  .letterhead-footer { position: absolute; left: 0; bottom: 0; width: 100%; height: 39px; background: var(--brand-blue); color: var(--paper); font-size: 8px; line-height: 11px; }
  .letterhead-footer .brand-square { position: absolute; left: 15px; top: 12px; width: 15px; height: 15px; }
  .footer-address { position: absolute; left: 48px; top: 9px; }
  .footer-phone { position: absolute; left: 303px; top: 9px; }
  .footer-web { position: absolute; left: 406px; top: 9px; }
  .label { display: inline-block; width: 11px; }

  /* Business cards */
  .card { position: absolute; width: 283px; height: 161px; overflow: hidden; }
  .card svg, .slip svg { position: absolute; left: 0; top: 0; }
  .card-front { left: 625px; top: 96px; }
  .card-front .brand-square { position: absolute; left: 139px; top: 124px; width: 18px; height: 18px; }
  .card-tagline { position: absolute; left: 174px; top: 122px; color: var(--paper); font-style: italic; font-weight: 700; font-size: 10px; line-height: 11px; }

  .card-back { left: 788px; top: 288px; }
  .card-back .brand { position: absolute; left: 17px; top: 118px; gap: 7px; }
  .card-back .brand-square { width: 14px; height: 14px; }
  .card-back .brand-name { font-size: 12px; }
  .contact-block { position: absolute; left: 182px; top: 15px; width: 84px; font-size: 6.2px; line-height: 9.5px; color: var(--ink); }
  .contact-name { font-weight: 700; font-size: 7px; }
  .contact-block hr { border: 0; border-top: 0.6px solid #999; margin: 4px 0; }
  .contact-block .label { width: 9px; font-weight: 700; }

  /* With compliments slip */
  .slip { position: absolute; left: 585px; top: 502px; width: 569px; height: 237px; overflow: hidden; }
  .slip .brand { position: absolute; left: 33px; top: 48px; gap: 16px; }
  .slip .brand-square { width: 34px; height: 34px; }
  .slip .brand-name { font-size: 32px; }
  .slip-address { position: absolute; left: 33px; top: 196px; color: var(--paper); font-size: 8.4px; line-height: 11px; }
  .slip-greeting { position: absolute; left: 433px; top: 196px; color: var(--brand-blue); font-family: "Dancing Script", cursive; font-size: 15px; }
</style>
</head>
<body>

<section class="letterhead">
  <header class="letterhead-header">
    <div class="brand">
      <span class="brand-square"></span>
      <span class="brand-name">KioskPlay Entertainment</span>
    </div>
  </header>
  <p class="salutation">Dear,</p>
  <p class="date-line">Date &nbsp;/ &nbsp;/</p>
  <div class="letter-body">
    <p class="indent">This is an Dummy language, Lorem ipsum dolor sit amet, consectetur adipiscing elit. Integer fermentum iaculis urna, ut fermentum dui euismod sit amet. Sed in feugiat lorem. Curabitur euismod massa at placerat gravida. Donec eros neque, mattis non malesuada vel, feugiat ut lacus. Cras euismod, velit sit amet venenatis faucibus, arcu nunc rutrum velit, sed condimentum arcu dolor vel augue.</p>
    <p>Lorem ipsum dolor sit amet, consectetur adipiscing elit. Integer fermentum iaculis urna, ut fermentum dui euismod sit amet. Sed in feugiat lorem. Curabitur euismod massa at placerat gravida. Donec eros neque, mattis non malesuada vel, feugiat ut lacus. Cras euismod, velit sit amet venenatis avida viverra a sem. Pellentesque scelerisque risus sed pulvinar facilisis.</p>
  </div>
  <p class="sign-off">Yours Faithfully<br>Name &amp; Signature here</p>
  <footer class="letterhead-footer">
    <span class="brand-square"></span>
    <p class="footer-address">Lorem ipsum dolor sit ameya Vestibulum &nbsp;47, suscipit laore<br>71336 cubilia Curae, tukamai rakalle, country 888 565 6=</p>
    <p class="footer-phone"><span class="label">P</span> 0253 4410270<br><span class="label">F</span> 0253 4410271</p>
    <p class="footer-web"><span class="label">E</span> info@kioskplay.com<br><span class="label">W</span> kioskplay.com</p>
  </footer>
</section>

<section class="card card-front">
  <svg width="283" height="161" viewBox="0 0 283 161">
    <defs>
      <clipPath id="front-white"><path d="M0,0 L162,0 A175,175 0 0 1 0,161 Z"/></clipPath>
    </defs>
    <rect width="283" height="161" fill="var(--paper)"/>
    <g clip-path="url(#front-white)">
      <rect x="8" y="10" width="170" height="115" rx="30" fill="var(--map-pale)" role="img" aria-label="Pale world map decoration"/>
    </g>
    <path d="M162,0 A175,175 0 0 1 0,161 L283,161 L283,0 Z" fill="var(--brand-blue)"/>
  </svg>
  <span class="brand-square"></span>
  <p class="card-tagline">Technology built for<br>Global Expansion</p>
</section>

<section class="card card-back">
  <svg width="283" height="161" viewBox="0 0 283 161">
    <defs>
      <clipPath id="back-white"><path d="M122,0 A200,200 0 0 0 265,161 L283,161 L283,0 Z"/></clipPath>
    </defs>
    <rect width="283" height="161" fill="var(--brand-blue)"/>
    <path d="M122,0 A200,200 0 0 0 265,161 L283,161 L283,0 Z" fill="var(--paper)"/>
    <g clip-path="url(#back-white)">
      <rect x="120" y="6" width="163" height="112" rx="30" fill="var(--map-pale)" opacity="0.6" role="img" aria-label="Pale world map decoration"/>
    </g>
  </svg>
  <div class="brand">
    <span class="brand-square"></span>
    <span class="brand-name">KioskPlay Entertainment</span>
  </div>
  <div class="contact-block">
    <p class="contact-name">Name of the person</p>
    <p>(Designation)</p>
    <hr>
    <p><span class="label">E</span>info@kioskplay.com</p>
    <p><span class="label">M</span>+00 00000 00000</p>
    <p><span class="label">W</span>www.kioskplay.com</p>
    <hr>
    <p>Lorem ipsum dolor sit ameya Vestibulum &nbsp;47, suscipit laore 71336 cubilia Curae</p>
  </div>
</section>

<section class="slip">
  <svg width="569" height="237" viewBox="0 0 569 237">
    <defs>
      <clipPath id="slip-blue"><path d="M0,0 L508,0 A260,260 0 0 1 295,237 L0,237 Z"/></clipPath>
    </defs>
    <rect width="569" height="237" fill="var(--brand-blue)"/>
    <g clip-path="url(#slip-blue)">
      <rect x="200" y="10" width="330" height="200" rx="60" fill="var(--map-on-blue)" role="img" aria-label="World map decoration in light blue"/>
    </g>
    <path d="M508,0 A260,260 0 0 1 295,237 L569,237 L569,0 Z" fill="var(--paper)"/>
  </svg>
  <div class="brand">
    <span class="brand-square"></span>
    <span class="brand-name">KioskPlay Entertainment</span>
  </div>
  <p class="slip-address">Lorem ipsum dolor sit ameya Vestibulum &nbsp;47, suscipit laore<br>71336 cubilia Curae, tukamai rakalle, country 888 565 6=</p>
  <p class="slip-greeting">with complements...</p>
</section>

</body>
</html>
```